Brochure Design Project for Custom Embroidery (Monograms) Shop

The need is for an 8.5” x 11” single sheet (might be front and back, as required) to promote our company. Tilly’s Stitchworks, LLC provides personalization (monogramming) services as well as the items themselves, for business owners and consumers. Our company currently provides:
- Hats, Visors, Tee Shirts, Polo and Dress Shirts, Sweatshirts, Hoodies, Sports Wear (team clothing) Shorts and Shirts, etc
- Canvas Bags and Totes, Fleece Blankets and Throws, Backpacks, Reusable Grocery Bags, etc
- Men’s and Women’s zippered jackets, pull over jackets, Fleece jackets
- Children’s Shirts, Bibs, Towels
- Will work with customer’s current custom Logo
- Will work with customer to create new company logo
- Customer can view all items on website www.tillystitchworks.example (new site coming soon….)
Project needs to speak to three main concepts 1) Embroidery name, initials and logo on items, 2) [heat] Transfer names, initials, logos and graphics on items and 3) custom logo work.
Target market for this brochure (although we’d like to have it a little bit generic for other uses, if possible) is brand new business owners who have just purchased equipment to start their own business. These folk are attending training classes and this brochure will be a part of the training section that has to do with ‘creating your business image and start some Brand recognition’. The trainer will speak to the importance of them creating their own company image and this brochure will be placed in their take home material.
Things we like:
- White space
- Pictures / graphics of items, product and people
- A spot to input the ‘current’ special
- Our Company Logo and colors (red green beige)
- Spot in the brochure for the ‘current special’
- References to the web site
- Suitable for 3 hole punch (attention to the left margin)
- Professional appearance
Things not so good:
- Dark gloomy backgrounds
- Very tiny small text
Target Market(s)
business men and women starting their own business (easy text swaps for general public would be a huge plus)
Industry/Entity Type
Training
Look and feel

```html
<!DOCTYPE html>
<html lang="en">
<head>
<meta charset="utf-8">
<title>Tilly’s Stitchworks – Flyer</title>
<link rel="stylesheet" href="https://fonts.googleapis.com/css2?family=Parisienne&family=Arimo:wght@400;700&display=swap">
<style>
  :root {
    --brand-green: #1a9a4a;
    --leaf-green: #22a150;
    --berry-red: #e4474b;
    --page-top: #ffffff;
    --page-bottom: #ededed;
    --text-white: #ffffff;
    --canvas: #ffffff;
  }
  * { margin: 0; padding: 0; box-sizing: border-box; }
  html, body { width: 1200px; height: 1200px; overflow: hidden; background: var(--canvas); }
  .canvas { position: relative; width: 1200px; height: 1200px; overflow: hidden; }
  .page {
    position: absolute; left: 177px; top: 68px; width: 821px; height: 1065px;
    background: linear-gradient(var(--page-top), var(--page-bottom));
  }
  .shapes { position: absolute; inset: 0; }
  .brand-title {
    position: absolute; left: 548px; top: 118px;
    font-family: "Parisienne", cursive; color: var(--brand-green);
    font-size: 90px; line-height: 128px; font-weight: 400;
  }
  .brand-title span { display: block; white-space: nowrap; }
  .title-rule {
    position: absolute; left: 768px; top: 402px; width: 230px; height: 2px; background: var(--brand-green);
  }
  .contact {
    position: absolute; left: 777px; top: 412px; width: 210px;
    font-family: "Arimo", sans-serif; color: var(--brand-green);
  }
  .contact .owner { font-size: 13px; letter-spacing: 0.3px; margin-bottom: 12px; }
  .contact p { font-size: 11px; line-height: 16px; white-space: nowrap; }
  .partner {
    position: absolute; left: 558px; top: 440px;
    display: flex; align-items: center; gap: 8px;
    font-family: "Arimo", sans-serif; font-weight: 700; font-size: 17px; color: var(--brand-green);
  }
  .partner .dot { width: 22px; height: 22px; border-radius: 50%; background: var(--brand-green); }
  .offerings {
    position: absolute; left: 222px; top: 928px; width: 660px;
    font-family: "Arimo", sans-serif; color: var(--text-white);
  }
  .offerings h2 { font-size: 21px; line-height: 24px; font-weight: 700; margin: 0 0 5px 15px; }
  .offerings ul { list-style: none; }
  .offerings li { display: flex; align-items: center; gap: 6px; font-size: 11px; line-height: 15.5px; white-space: nowrap; }
  .offerings li svg { flex: none; }
  .site-note {
    position: absolute; left: 675px; top: 1098px;
    font-family: "Arimo", sans-serif; font-weight: 700; font-size: 19px; line-height: 22px; color: var(--brand-green);
  }
</style>
</head>
<body>
<div class="canvas">
  <div class="page"></div>

  <svg class="shapes" width="1200" height="1200" viewBox="0 0 1200 1200">
    <defs>
      <linearGradient id="polo-tones" x1="0" y1="0" x2="0" y2="1">
        <stop offset="0" stop-color="#8fae6e"/>
        <stop offset="0.45" stop-color="#2f8a45"/>
        <stop offset="1" stop-color="#1f7a3a"/>
      </linearGradient>
      <linearGradient id="tote-tones" x1="0" y1="0" x2="1" y2="1">
        <stop offset="0" stop-color="#f3a9c8"/>
        <stop offset="0.5" stop-color="#f2ece0"/>
        <stop offset="1" stop-color="#ea8fb7"/>
      </linearGradient>
      <linearGradient id="berry-tones" x1="0" y1="0" x2="1" y2="1">
        <stop offset="0" stop-color="#2aa352"/>
        <stop offset="0.5" stop-color="#e4474b"/>
        <stop offset="1" stop-color="#d83c42"/>
      </linearGradient>
    </defs>

    <rect class="emblem-art" x="245" y="82" width="268" height="325" rx="40" fill="url(#berry-tones)" opacity="0.85"
          role="img" aria-label="Illustration of three strawberries hanging on a curling green vine"/>

    <path class="photo-leaf photo-leaf--polo" role="img" aria-label="Photo of a man wearing an embroidered green polo shirt"
          d="M236 432 C 400 430 560 520 582 680 C 592 760 560 812 490 814 C 380 816 300 760 262 650 C 236 570 230 500 236 432 Z"
          fill="url(#polo-tones)" stroke="var(--leaf-green)" stroke-width="8"/>

    <path class="photo-leaf photo-leaf--tote" role="img" aria-label="Photo of a hand carrying a pink and natural canvas tote bag"
          d="M936 534 C 780 536 630 600 604 760 C 594 840 630 904 700 906 C 800 908 880 850 912 740 C 934 670 940 600 936 534 Z"
          fill="url(#tote-tones)" stroke="var(--leaf-green)" stroke-width="8"/>

    <path class="offer-leaf"
          d="M177 1000 C 185 925 320 896 520 893 C 700 890 880 894 998 902 L 998 1133 C 968 1100 935 1088 860 1087 C 650 1085 420 1090 270 1090 C 205 1088 177 1050 177 1000 Z"
          fill="var(--leaf-green)"/>
  </svg>

  <h1 class="brand-title"><span>Tilly’s</span><span>Stitchworks</span></h1>
  <div class="title-rule"></div>

  <div class="partner"><span class="dot"></span>Brightway Vending</div>

  <div class="contact">
    <p class="owner">NORA WHITFIELD</p>
    <p>(800) 555-0142</p>
    <p>(614) 555-0187 FAX</p>
    <p>INFO@TILLYSTITCHWORKS.EXAMPLE</p>
    <p>WWW.TILLYSTITCHWORKS.EXAMPLE</p>
  </div>

  <section class="offerings">
    <h2>Our company currently provides:</h2>
    <ul>
      <li><svg width="12" height="10" viewBox="0 0 12 10"><path d="M1 5 L4.5 8.5 L11 1" fill="none" stroke="#fff" stroke-width="2"/></svg>Hats, Visors, Tee Shirts, Polo and Dress Shirts, Sweatshirts, Hoodies, Sports Wear (team clothing) Shorts and Shirts, etc</li>
      <li><svg width="12" height="10" viewBox="0 0 12 10"><path d="M1 5 L4.5 8.5 L11 1" fill="none" stroke="#fff" stroke-width="2"/></svg>Canvas Bags and Totes, Fleece Blankets and Throws, Backpacks, Reusable Grocery Bags, etc</li>
      <li><svg width="12" height="10" viewBox="0 0 12 10"><path d="M1 5 L4.5 8.5 L11 1" fill="none" stroke="#fff" stroke-width="2"/></svg>Men’s and Women’s zippered jackets, pull over jackets, Fleece jackets</li>
      <li><svg width="12" height="10" viewBox="0 0 12 10"><path d="M1 5 L4.5 8.5 L11 1" fill="none" stroke="#fff" stroke-width="2"/></svg>Children’s Shirts, Bibs, Towels</li>
      <li><svg width="12" height="10" viewBox="0 0 12 10"><path d="M1 5 L4.5 8.5 L11 1" fill="none" stroke="#fff" stroke-width="2"/></svg>Will work with customer’s current custom Logo</li>
      <li><svg width="12" height="10" viewBox="0 0 12 10"><path d="M1 5 L4.5 8.5 L11 1" fill="none" stroke="#fff" stroke-width="2"/></svg>Will work with customer to create new company logo</li>
      <li><svg width="12" height="10" viewBox="0 0 12 10"><path d="M1 5 L4.5 8.5 L11 1" fill="none" stroke="#fff" stroke-width="2"/></svg>Customer can view all items on website www.tillystitchworks.example</li>
    </ul>
  </section>

  <p class="site-note">(new site coming soon….)</p>
</div>
</body>
</html>
```